Need Bus charter business website,

I am starting a bus charter business in the near future. I am based in Geelong, Victoria in Australia. I will have a 25 or 28 seater bus that will be used to take people on charted trips. Whether they be to birthday parties, weddings, sporting events, corporate events, mystery trips, going down the Great Ocean Road, or anywhere someone wants. As for colour scheme, I'm leaning towards something blue and grey, but open to anything really that catches my eye. I played around with a basic web design program and made a basic site which I uploaded ( www.kelvomtravel.com.au) It has things which I wanted to include such as, services I will provide, trip information, contact form etc.

I don't mind if the layout is completely different to my site as it was only a template that was included in the program I used. I would like the overall design to be relatively fluid, not having to back-track a lot to navigate the site.

```html
<!DOCTYPE html>
<html lang="en">
<head>
<meta charset="utf-8">
<title>Kelvom Travel – Bus Charter Geelong</title>
<link rel="stylesheet" href="https://fonts.googleapis.com/css2?family=Raleway:wght@300;400;500;600;700&family=Open+Sans:wght@400;600&display=swap">
<style>
:root{
  --blue:#0aa6d6;
  --blue-dark:#0790bb;
  --ink:#1a1a1a;
  --text:#333;
  --muted:#8a8a8a;
  --field:#e4e4e4;
  --night:#0c0d0f;
  --caption:#2a2b2d;
  --white:#fff;
}
*{box-sizing:border-box;margin:0;padding:0}
html,body{width:820px;height:1200px;overflow:hidden;background:var(--white)}
body{position:relative;font-family:"Open Sans",Arial,sans-serif;color:var(--text)}
.abs{position:absolute}

/* header */
.site-header{left:0;top:0;width:820px;height:66px}
.brand{left:118px;top:14px;font-family:"Raleway",Arial,sans-serif;font-weight:600;font-size:21px;color:var(--ink);letter-spacing:.5px;display:flex;align-items:center;gap:8px}
.brand-mark{width:12px;height:12px;background:var(--blue)}
.call{left:600px;top:8px;width:112px;text-align:center;font-family:"Raleway",Arial,sans-serif}
.call svg{display:block;margin:0 auto 1px}
.call-label{font-size:11px;color:var(--ink)}
.call-number{font-size:11px;color:var(--blue)}

/* nav */
.main-nav{left:0;top:66px;width:820px;height:48px;background:var(--blue)}
.main-nav ul{list-style:none;position:absolute;left:118px;top:0;height:48px;display:flex;border-left:1px solid rgba(255,255,255,.22)}
.main-nav li{height:48px;display:flex;align-items:center;justify-content:center;border-right:1px solid rgba(255,255,255,.22);font-family:"Raleway",Arial,sans-serif;font-size:8.5px;font-weight:500;color:var(--white);letter-spacing:.4px}

/* hero */
.hero{left:0;top:114px;width:820px;height:276px;background:linear-gradient(100deg,#8fb2c9 0%,#c9d6de 18%,#e9eef1 32%,#5a6b55 55%,#46523d 70%,#2d2f2c 100%)}
.hero-shade{position:absolute;inset:0;background:linear-gradient(90deg,rgba(0,0,0,0) 45%,rgba(0,0,0,.35) 100%)}
.hero-kicker{right:115px;top:95px;font-family:"Raleway",Arial,sans-serif;font-weight:300;font-size:22px;color:var(--white);letter-spacing:.5px}
.hero-title{right:115px;top:117px;font-family:"Raleway",Arial,sans-serif;font-weight:700;font-size:35px;color:var(--white);letter-spacing:.3px}
.hero-btn{left:611px;top:164px;width:92px;height:37px;background:var(--blue);color:var(--white);font-family:"Raleway",Arial,sans-serif;font-size:11.5px;display:flex;align-items:center;justify-content:center}
.hero-arrow{top:115px}
.hero-dots{left:397px;top:253px;display:flex;gap:3px}
.hero-dots span{width:5px;height:5px;border-radius:50%;background:rgba(255,255,255,.5)}
.hero-dots span:first-child{background:var(--white)}

/* booking */
.booking-title{left:0;top:402px;width:820px;text-align:center;font-family:"Raleway",Arial,sans-serif;font-size:24px;color:var(--blue);font-weight:400}
.field-label{font-family:"Raleway",Arial,sans-serif;font-size:8.5px;color:var(--ink);letter-spacing:.2px}
.field{height:24px;background:var(--field);border:1px solid #d8d8d8;font-size:6.5px;color:var(--muted);padding-left:9px;display:flex;align-items:center;justify-content:space-between;padding-right:8px;font-family:"Raleway",Arial,sans-serif}
.book-btn{left:483px;top:501px;width:214px;height:36px;background:var(--blue);color:var(--white);font-family:"Raleway",Arial,sans-serif;font-size:12px;display:flex;align-items:center;justify-content:center;letter-spacing:.3px}

/* features */
.features{left:0;top:558px;width:820px;height:258px;background:radial-gradient(ellipse at 50% 45%,#26292c 0%,#121315 60%,var(--night) 100%)}
.features-title{left:0;top:20px;width:820px;text-align:center;font-family:"Raleway",Arial,sans-serif;font-size:20.5px;line-height:24px}
.features-title .accent{color:var(--blue)}
.features-title .plain{color:var(--white)}
.feature{top:78px;width:80px;text-align:center}
.feature-icon{width:58px;height:58px;border-radius:50%;background:var(--blue);margin:0 auto;display:flex;align-items:center;justify-content:center}
.feature-name{margin-top:9px;font-family:"Raleway",Arial,sans-serif;font-size:9.5px;color:var(--white)}
.features-copy{left:190px;top:162px;width:440px;text-align:center;font-size:8.2px;line-height:11.5px;color:var(--white)}
.features-btn{left:369px;top:208px;width:90px;height:27px;background:var(--blue);color:var(--white);font-family:"Raleway",Arial,sans-serif;font-size:7.5px;font-weight:600;display:flex;align-items:center;justify-content:center}

/* cards */
.card{top:838px;width:278px;height:135px}
.card-photo{position:absolute;left:0;top:0;width:253px;height:92px}
.card-arrow{position:absolute;right:0;top:0;width:25px;height:92px;background:var(--blue);display:flex;align-items:center;justify-content:center}
.card-caption{position:absolute;left:0;top:92px;width:278px;height:43px;background:var(--caption);text-align:center}
.card-title{font-family:"Raleway",Arial,sans-serif;font-size:18px;color:var(--blue);margin-top:4px;line-height:22px}
.card-tags{font-size:6.6px;color:var(--white);letter-spacing:.2px;font-family:"Raleway",Arial,sans-serif}

/* footer */
.site-footer{left:0;top:995px;width:820px;height:175px;background:linear-gradient(180deg,#121315 0%,#1c1e20 50%,#0f1011 100%)}
.footer-col{top:22px}
.footer-heading{font-family:"Raleway",Arial,sans-serif;font-size:15.5px;color:var(--blue);font-weight:400}
.footer-menu{list-style:none;margin-top:12px;width:128px}
.footer-menu li{font-family:"Raleway",Arial,sans-serif;font-size:7px;color:var(--white);padding:4px 0 6px 10px;border-bottom:1px solid #3a3c3f;position:relative}
.footer-menu li::before{content:"";position:absolute;left:2px;top:8px;width:2px;height:2px;background:var(--white)}
.social-list{list-style:none;margin-top:10px;width:104px}
.social-list li{display:flex;justify-content:space-between;align-items:center;height:21px;font-family:"Raleway",Arial,sans-serif;font-size:7px;color:var(--white)}
.social-dot{width:7px;height:7px;border-radius:50%;background:#4b4e52}
.divider{width:1px;background:#2e3033}
.news-item{width:104px;margin-top:10px}
.news-head{font-family:"Raleway",Arial,sans-serif;font-size:7px;color:var(--white);padding-left:8px;position:relative;padding-bottom:4px;border-bottom:1px solid #3a3c3f}
.news-head::before{content:"";position:absolute;left:1px;top:4px;width:2px;height:2px;background:var(--white)}
.news-text{font-size:6px;color:#9a9a9a;line-height:8.5px;margin-top:6px;padding-left:3px}
.blog-item{display:flex;align-items:center;gap:5px;margin-top:9px}
.blog-thumb{width:43px;height:36px;background:linear-gradient(135deg,#6f8fa8,#c9c2a6 55%,#55606a)}
.blog-name{font-family:"Raleway",Arial,sans-serif;font-size:7px;color:var(--white)}

/* bottom bar */
.bottom-bar{left:0;top:1170px;width:820px;height:30px;display:flex;align-items:center;justify-content:center;font-family:"Raleway",Arial,sans-serif;font-size:8.5px;color:var(--ink);gap:4px}
</style>
</head>
<body>

<header class="site-header abs">
  <div class="brand abs"><span class="brand-mark"></span>Kelvom Travel</div>
  <div class="call abs">
    <svg width="16" height="12" viewBox="0 0 16 12"><path d="M2 4 Q8 -1 14 4 L12.5 6 L10.5 5 L10.5 3.5 Q8 2.7 5.5 3.5 L5.5 5 L3.5 6 Z" fill="#0aa6d6"/><rect x="4" y="6" width="8" height="5" rx="1" fill="#0aa6d6"/></svg>
    <div class="call-label">Call Us Now !</div>
    <div class="call-number">( 0800-555-0199 )</div>
  </div>
</header>

<nav class="main-nav abs">
  <ul>
    <li style="width:87px">HOME</li>
    <li style="width:93px">ABOUT</li>
    <li style="width:100px">BOOKING</li>
    <li style="width:95px">OFFERS</li>
    <li style="width:103px">SERVICES</li>
    <li style="width:107px">CONTACT</li>
  </ul>
</nav>

<section class="hero abs" role="img" aria-label="White touring coach on a coastal road beside the sea and green hills">
  <div class="hero-shade"></div>
  <div class="hero-kicker abs">MAKING TRANSPORTATION</div>
  <div class="hero-title abs">FAST AND SAFE !</div>
  <div class="hero-btn abs">Read More</div>
  <svg class="hero-arrow abs" style="left:33px" width="44" height="44" viewBox="0 0 44 44"><circle cx="22" cy="22" r="20.5" fill="none" stroke="#fff" stroke-width="2"/><path d="M25 13 L16 22 L25 31" fill="none" stroke="#fff" stroke-width="2"/></svg>
  <svg class="hero-arrow abs" style="left:739px" width="44" height="44" viewBox="0 0 44 44"><circle cx="22" cy="22" r="20.5" fill="none" stroke="#fff" stroke-width="2"/><path d="M19 13 L28 22 L19 31" fill="none" stroke="#fff" stroke-width="2"/></svg>
  <div class="hero-dots abs"><span></span><span></span><span></span></div>
</section>

<section class="booking">
  <h2 class="booking-title abs">BOOK MY BUS !</h2>

  <div class="field-label abs" style="left:125px;top:447px">FROM</div>
  <div class="field abs" style="left:125px;top:462px;width:108px">SELECT<span>&#8964;</span></div>
  <div class="field-label abs" style="left:237px;top:447px">TO</div>
  <div class="field abs" style="left:237px;top:462px;width:108px">SELECT<span>&#8964;</span></div>
  <div class="field-label abs" style="left:357px;top:447px">DEPART ON</div>
  <div class="field abs" style="left:357px;top:462px;width:108px">05-05-2015<span>&#8661;</span></div>
  <div class="field-label abs" style="left:469px;top:447px">PASSENGERS</div>
  <div class="field abs" style="left:469px;top:462px;width:108px">05<span>&#8661;</span></div>
  <div class="field-label abs" style="left:589px;top:447px">SITTING OPTION</div>
  <div class="field abs" style="left:589px;top:462px;width:108px">ANY<span>&#8964;</span></div>

  <div class="field-label abs" style="left:125px;top:502px">DEPARTURE TIME</div>
  <div class="field abs" style="left:125px;top:515px;width:108px">ANY TIME<span>&#8964;</span></div>
  <div class="field-label abs" style="left:237px;top:502px">BUS TYPE</div>
  <div class="field abs" style="left:237px;top:515px;width:108px">ANY BUS<span>&#8964;</span></div>
  <div class="field-label abs" style="left:357px;top:502px">MORE OPTION</div>
  <div class="field abs" style="left:357px;top:515px;width:108px">SELECT<span>&#8964;</span></div>

  <div class="book-btn abs">BOOK NOW !</div>
</section>

<section class="features abs">
  <h2 class="features-title abs"><span class="accent">Explore Your Favorite Destination With</span><br><span class="plain">Style And Comfort!</span></h2>

  <div class="feature abs" style="left:230px">
    <div class="feature-icon"><svg width="26" height="26" viewBox="0 0 26 26"><path d="M5 19 A9.5 9.5 0 1 1 21 19" fill="none" stroke="#fff" stroke-width="2.2"/><path d="M13 15 L18 10" stroke="#fff" stroke-width="2.2"/><circle cx="13" cy="15" r="2" fill="#fff"/></svg></div>
    <div class="feature-name">FAST</div>
  </div>
  <div class="feature abs" style="left:325px">
    <div class="feature-icon"><svg width="24" height="26" viewBox="0 0 24 26"><path d="M12 2 L21 5 L21 12 Q21 20 12 24 Q3 20 3 12 L3 5 Z" fill="#fff"/><path d="M8 13 L11 16 L16 9" fill="none" stroke="#0aa6d6" stroke-width="2"/></svg></div>
    <div class="feature-name">SAFE</div>
  </div>
  <div class="feature abs" style="left:419px">
    <div class="feature-icon"><svg width="26" height="26" viewBox="0 0 26 26"><circle cx="13" cy="13" r="9" fill="none" stroke="#fff" stroke-width="2.2"/><path d="M7 16 Q13 9 19 16" fill="none" stroke="#fff" stroke-width="2.2"/><circle cx="13" cy="9" r="2" fill="#fff"/></svg></div>
    <div class="feature-name">COMFORT</div>
  </div>
  <div class="feature abs" style="left:513px">
    <div class="feature-icon"><svg width="28" height="22" viewBox="0 0 28 22"><path d="M2 8 L8 4 L14 8 L20 4 L26 8 L24 12 L16 18 L12 18 L4 12 Z" fill="none" stroke="#fff" stroke-width="2" stroke-linejoin="round"/><path d="M10 11 L14 14 M13 9 L17 12" stroke="#fff" stroke-width="1.6"/></svg></div>
    <div class="feature-name">SERVICE</div>
  </div>

  <p class="features-copy abs">We are an accredited bus company that operates bus trip and charter work in the Geelong area. We offer a range of services, from day trips down the Great Ocean Road, to transport for wedding guests, Buck's and Hen's nights or school trips.</p>
  <div class="features-btn abs">READ MORE</div>
</section>

<article class="card abs" style="left:127px">
  <div class="card-photo" role="img" aria-label="Group of travellers standing beside a parked coach in a leafy park" style="background:linear-gradient(135deg,#4f7a3a 0%,#8caa6a 40%,#d9dcd6 70%,#9aa3a9 100%)"></div>
  <div class="card-arrow"><svg width="10" height="16" viewBox="0 0 10 16"><path d="M2 2 L8 8 L2 14" fill="none" stroke="#fff" stroke-width="1.8"/></svg></div>
  <div class="card-caption">
    <div class="card-title">BOOK A BUS FOR !</div>
    <div class="card-tags">FUNCTION , BIRTHDAY PARTIES , SPORTING EVENTS , MYSTRY TRIP</div>
  </div>
</article>

<article class="card abs" style="left:415px">
  <div class="card-photo" role="img" aria-label="White double-deck coach parked on a sunny forecourt" style="background:linear-gradient(180deg,#9fc4de 0%,#e6eef2 45%,#f4f4f4 65%,#a9aeb1 100%)"></div>
  <div class="card-arrow"><svg width="10" height="16" viewBox="0 0 10 16"><path d="M2 2 L8 8 L2 14" fill="none" stroke="#fff" stroke-width="1.8"/></svg></div>
  <div class="card-caption">
    <div class="card-title">WANT TO BOOK A TRIP?</div>
    <div class="card-tags">FUNCTION , BIRTHDAY PARTIES , SPORTING EVENTS , MYSTRY TRIP</div>
  </div>
</article>

<footer class="site-footer abs">
  <div class="footer-col abs" style="left:120px">
    <h3 class="footer-heading">MENU</h3>
    <ul class="footer-menu">
      <li>HOME</li><li>ABOUT</li><li>SERVICE</li><li>BOOKING</li><li>CONTACT</li>
    </ul>
  </div>
  <div class="divider abs" style="left:247px;top:38px;height:110px"></div>
  <div class="footer-col abs" style="left:274px">
    <h3 class="footer-heading">SOCIAL</h3>
    <ul class="social-list">
      <li><span class="social-dot"></span>CIRCLEBOOK</li>
      <li><span class="social-dot"></span>CHIRPER</li>
      <li><span class="social-dot"></span>GATHER PLUS</li>
      <li><span class="social-dot"></span>PINSPIRE</li>
    </ul>
  </div>
  <div class="divider abs" style="left:404px;top:38px;height:110px"></div>
  <div class="footer-col abs" style="left:433px">
    <h3 class="footer-heading">NEWS</h3>
    <div class="news-item">
      <div class="news-head">KELVOM TRAVEL :</div>
      <div class="news-text">We are an accredited bus comp any that operates</div>
    </div>
    <div class="news-item" style="margin-top:6px">
      <div class="news-head">KELVOM TRAVEL :</div>
      <div class="news-text">We are an accredited bus comp any that operates</div>
    </div>
  </div>
  <div class="divider abs" style="left:564px;top:38px;height:110px"></div>
  <div class="footer-col abs" style="left:590px">
    <h3 class="footer-heading">BLOG</h3>
    <div class="blog-item"><div class="blog-thumb" role="img" aria-label="Passengers gathered by a coach"></div><span class="blog-name">KELVOM TRAVEL :</span></div>
    <div class="blog-item" style="margin-top:2px"><div class="blog-thumb" role="img" aria-label="Coach parked outdoors"></div><span class="blog-name">KELVOM TRAVEL :</span></div>
  </div>
</footer>

<div class="bottom-bar abs">KELVOM TRAVEL © 2014.&nbsp; <span>Privacy Policy</span></div>

</body>
</html>
```